MORVEK IT Limited Buisness card logo

I am setting up a IT Consultancy company and want a logo that is related to the IT industry, but also i am thinking that the A in MOR and the A in VEK are linked together maybe horizontally and vertically, also thought about the A being @ as it symbolises IT services. This logo will be used on paperwork, business cards and website.

Industry/Entity Type

Business

Contact Information for Business Card

Gareth Wilmslow
MORVEK IT Limited
IT Consultant
Mobile: 07912563084
Email: garethwk@fernmail.co.uk

Requirements
Must have
• IT Theme

```html
<!DOCTYPE html>
<html lang="en">
<head>
<meta charset="utf-8">
<title>MORVEK IT – Business Card</title>
<link rel="stylesheet" href="https://fonts.googleapis.com/css2?family=Quicksand:wght@500;700&display=swap">
<style>
  :root {
    --brand-blue: #0d58a8;
    --card-blue-light: #1a76c9;
    --card-blue-dark: #0a2f6e;
    --steel-dark: #4a4e54;
    --steel-mid: #8a8e94;
    --steel-light: #d9dce0;
    --page-white: #ffffff;
    --stage-grey: #eceef1;
    --text-white: #ffffff;
    --text-soft: #d6e6f7;
  }
  * { margin: 0; padding: 0; box-sizing: border-box; }
  html, body { width: 1200px; height: 1172px; overflow: hidden; }
  body {
    font-family: "Quicksand", sans-serif;
    background: var(--stage-grey);
    position: relative;
  }
  .logo-band {
    position: absolute; left: 0; top: 0;
    width: 1200px; height: 280px;
    background: var(--page-white);
    display: flex; align-items: center; justify-content: center;
  }
  .wordmark {
    font-family: "Quicksand", sans-serif;
    font-weight: 700;
    font-size: 96px;
    letter-spacing: 4px;
    color: var(--brand-blue);
  }
  .business-card {
    position: absolute;
    left: 180px; top: 420px;
    width: 840px; height: 480px;
    overflow: hidden;
    box-shadow: 0 18px 40px rgba(0,0,0,0.18);
    display: flex;
  }
  .card-panel {
    position: relative;
    width: 640px; height: 480px;
    background: linear-gradient(135deg, var(--card-blue-dark) 0%, var(--card-blue-light) 45%, var(--card-blue-dark) 100%);
  }
  .card-decoration {
    width: 200px; height: 480px;
    background: linear-gradient(135deg, var(--steel-dark) 0%, var(--steel-light) 50%, var(--steel-mid) 100%);
  }
  .card-content {
    position: absolute; left: 70px; top: 56px;
    color: var(--text-white);
  }
  .card-wordmark {
    font-weight: 700; font-size: 54px; letter-spacing: 2px;
  }
  .holder-name {
    margin-top: 56px;
    font-weight: 500; font-size: 40px;
  }
  .holder-role {
    font-weight: 500; font-size: 26px;
    color: var(--text-soft);
    margin-top: 2px;
  }
  .contact-list { list-style: none; margin-top: 52px; }
  .contact-item {
    display: flex; align-items: center; gap: 16px;
    font-weight: 500; font-size: 26px;
    margin-bottom: 14px;
    white-space: nowrap;
  }
  .contact-icon { width: 36px; height: 36px; flex: none; }
</style>
</head>
<body>
  <header class="logo-band">
    <div class="wordmark">MORVEK IT</div>
  </header>

  <section class="business-card">
    <div class="card-panel">
      <div class="card-content">
        <div class="card-wordmark">MORVEK IT</div>
        <h1 class="holder-name">Gareth Wilmslow</h1>
        <p class="holder-role">IT Consultant</p>
        <ul class="contact-list">
          <li class="contact-item">
            <svg class="contact-icon" viewBox="0 0 36 36" aria-hidden="true">
              <circle cx="18" cy="18" r="16" fill="none" stroke="#fff" stroke-width="2"/>
              <rect x="13" y="8" width="10" height="20" rx="2" fill="none" stroke="#fff" stroke-width="2"/>
              <line x1="16" y1="24" x2="20" y2="24" stroke="#fff" stroke-width="2"/>
            </svg>
            <span>07912563084</span>
          </li>
          <li class="contact-item">
            <svg class="contact-icon" viewBox="0 0 36 36" aria-hidden="true">
              <circle cx="18" cy="18" r="16" fill="none" stroke="#fff" stroke-width="2"/>
              <rect x="9" y="12" width="18" height="12" fill="none" stroke="#fff" stroke-width="2"/>
              <polyline points="9,12 18,19 27,12" fill="none" stroke="#fff" stroke-width="2"/>
            </svg>
            <span>garethwk@fernmail.co.uk</span>
          </li>
        </ul>
      </div>
    </div>
    <div class="card-decoration" role="img" aria-label="Decorative metallic band artwork in dark and silver grey tones"></div>
  </section>
</body>
</html>
```